Business Card Design Project

I am opening my own real estate company.

Tarrow & Co. Real Estate Inc.

See attachments for ideas and colors…..
Updates

Project Deadline Extended
Reason: I paid for 5 separate items (graphic design, logo, stationery, brochure & website) all at one time. I thought they all launched at the same time but they did not. That is the reason I have to extend the date.

Target Market(s)

High end real estate properties.

Industry/Entity Type

Real Estate

Font styles to use
Serif
Decorative
Script

Requirements
Must have
• High end design. I want to appeal to very expensive properties.

```html
<!DOCTYPE html>
<html lang="en">
<head>
<meta charset="utf-8">
<title>Tarrow &amp; Co. Real Estate Inc. — Business Cards</title>
<link rel="stylesheet" href="https://fonts.googleapis.com/css2?family=Cormorant+Garamond:wght@500;700&display=swap">
<style>
  :root {
    --page: #3a3a3a;
    --card-dark-top: #2a2a2a;
    --card-dark-mid: #4a4a4a;
    --card-stripe: #333333;
    --band: #b9b9bb;
    --ink: #1c1c1c;
    --gold: #ddd77c;
    --silver: #c4c4c4;
  }
  html, body {
    margin: 0;
    width: 1200px;
    height: 634px;
    overflow: hidden;
    background: var(--page);
    font-family: "Cormorant Garamond", Georgia, serif;
  }
  .canvas {
    position: relative;
    width: 1200px;
    height: 634px;
  }
  .card {
    position: absolute;
    top: 167px;
    width: 520px;
    height: 300px;
    border-radius: 22px;
    overflow: hidden;
    box-shadow: 0 10px 24px rgba(0,0,0,.45);
  }
  .card--gold { left: 50px; background: radial-gradient(ellipse at 55% 30%, var(--card-dark-mid), var(--card-dark-top) 70%); }
  .card--silver { left: 630px; background: linear-gradient(180deg, var(--card-stripe), var(--card-dark-top)); }
  .city-band {
    position: absolute;
    left: 0;
    right: 0;
    bottom: 0;
    height: 112px;
    background: var(--band);
  }
  .brand {
    position: absolute;
    top: 82px;
    left: 0;
    right: 0;
    display: flex;
    justify-content: center;
    align-items: center;
    gap: 14px;
    font-size: 27px;
    font-weight: 500;
    letter-spacing: .3px;
    white-space: nowrap;
  }
  .brand__dot { width: 14px; height: 14px; border-radius: 50%; }
  .card--gold .brand { color: var(--gold); }
  .card--gold .brand__dot { background: var(--gold); }
  .card--silver .brand { color: var(--silver); }
  .card--silver .brand__dot { background: var(--silver); }
  .holder {
    position: absolute;
    left: 42px;
    top: 222px;
    font-size: 21px;
    font-weight: 700;
    color: var(--ink);
  }
  .divider {
    position: absolute;
    left: 200px;
    top: 212px;
    width: 1px;
    height: 72px;
    background: var(--ink);
  }
  .contacts {
    position: absolute;
    left: 212px;
    top: 211px;
    margin: 0;
    padding: 0;
    list-style: none;
    font-size: 19px;
    font-weight: 500;
    line-height: 24px;
    color: var(--ink);
  }
  .contacts li { display: flex; align-items: center; gap: 8px; }
  .contacts svg { width: 12px; height: 12px; flex: none; }
</style>
</head>
<body>
<main class="canvas">

  <section class="card card--gold">
    <div class="city-band" role="img" aria-label="City skyline silhouette in light grey"></div>
    <div class="brand"><span class="brand__dot"></span>Tarrow &amp; Co. Real Estate Inc.</div>
    <div class="holder">Your name</div>
    <div class="divider"></div>
    <ul class="contacts">
      <li><svg viewBox="0 0 12 12"><rect x="1" y="3" width="10" height="7" fill="none" stroke="currentColor"/><polyline points="1,3 6,7 11,3" fill="none" stroke="currentColor"/></svg>yourmail@tarrowco.com</li>
      <li><svg viewBox="0 0 12 12"><circle cx="6" cy="6" r="5" fill="none" stroke="currentColor"/><line x1="1" y1="6" x2="11" y2="6" stroke="currentColor"/><ellipse cx="6" cy="6" rx="2.2" ry="5" fill="none" stroke="currentColor"/></svg>www.tarrowrealestate.com</li>
      <li><svg viewBox="0 0 12 12"><circle cx="6" cy="6" r="5" fill="none" stroke="currentColor"/><path d="M4 3.5 L5 5 L4.5 6 Q5.5 7.5 6.5 8 L7.5 7.5 L9 8.5" fill="none" stroke="currentColor"/></svg>(555) 214-3087</li>
    </ul>
  </section>

  <section class="card card--silver">
    <div class="city-band" role="img" aria-label="City skyline silhouette in light grey"></div>
    <div class="brand"><span class="brand__dot"></span>Tarrow &amp; Co. Real Estate Inc.</div>
    <div class="holder">Your name</div>
    <div class="divider"></div>
    <ul class="contacts">
      <li><svg viewBox="0 0 12 12"><rect x="1" y="3" width="10" height="7" fill="none" stroke="currentColor"/><polyline points="1,3 6,7 11,3" fill="none" stroke="currentColor"/></svg>yourmail@tarrowco.com</li>
      <li><svg viewBox="0 0 12 12"><circle cx="6" cy="6" r="5" fill="none" stroke="currentColor"/><line x1="1" y1="6" x2="11" y2="6" stroke="currentColor"/><ellipse cx="6" cy="6" rx="2.2" ry="5" fill="none" stroke="currentColor"/></svg>www.tarrowrealestate.com</li>
      <li><svg viewBox="0 0 12 12"><circle cx="6" cy="6" r="5" fill="none" stroke="currentColor"/><path d="M4 3.5 L5 5 L4.5 6 Q5.5 7.5 6.5 8 L7.5 7.5 L9 8.5" fill="none" stroke="currentColor"/></svg>(555) 214-3087</li>
    </ul>
  </section>

</main>
</body>
</html>
```